Needing a business Card for new fire company.

Dulvan, sales fire equipment and parts. We also do tree clearing for the forest service. My logo will be attached to this. I am also looking for a design that when people see the card it stick with them and they will remember my sales team giving it to them.

```html
<!DOCTYPE html>
<html lang="en">
<head>
<meta charset="utf-8">
<title>Dulvan Business Card</title>
<link rel="stylesheet" href="https://fonts.googleapis.com/css2?family=Montserrat:wght@400;500;600;700;800&display=swap">
<style>
  :root {
    --backdrop: #c6c6c6;
    --card-light: #e2e2e4;
    --brand-red: #b01f2a;
    --brand-red-soft: #bb3640;
    --ink: #141414;
    --paper-text: #ecdfe0;
  }
  * { margin: 0; padding: 0; box-sizing: border-box; }
  html, body { width: 1200px; height: 1101px; overflow: hidden; }
  body {
    background: var(--backdrop);
    font-family: "Montserrat", sans-serif;
    position: relative;
  }
  .card {
    position: absolute;
    top: 266px;
    width: 302px;
    height: 533px;
    overflow: hidden;
  }
  .card--front { left: 246px; background: var(--card-light); color: var(--ink); text-align: center; }
  .card--back { left: 641px; background: var(--brand-red); color: var(--paper-text); text-align: center; }

  .front__item { position: absolute; left: 0; width: 100%; }
  .name-first { top: 58px; font-size: 26px; font-weight: 700; letter-spacing: 0.2px; }
  .name-last { top: 91px; font-size: 26px; font-weight: 700; color: var(--brand-red); }
  .job-title { top: 136px; font-size: 14px; font-weight: 600; letter-spacing: 0.5px; }
  .divider { position: absolute; left: 109px; width: 84px; height: 2px; background: var(--ink); border-radius: 50%; }
  .divider--top { top: 173px; }
  .divider--bottom { top: 359px; }

  .contact-icon { position: absolute; left: 142px; width: 18px; height: 18px; }
  .contact-icon--phone { top: 196px; }
  .contact-icon--mail { top: 249px; }
  .contact-icon--web { top: 299px; }
  .contact-text { font-size: 14px; font-weight: 600; letter-spacing: 0.2px; }
  .contact-text--phone { top: 220px; }
  .contact-text--mail { top: 271px; }
  .contact-text--web { top: 321px; }

  .wordmark { top: 420px; font-size: 38px; font-weight: 800; letter-spacing: 2px; color: var(--ink); }

  .ring-art {
    position: absolute; left: 169px; top: 0; width: 133px; height: 160px;
    background: radial-gradient(circle at 100% 0%, var(--brand-red-soft) 0%, var(--brand-red) 100%);
  }
  .flame-art {
    position: absolute; left: 12px; top: 395px; width: 290px; height: 128px;
    background: linear-gradient(to top, var(--brand-red-soft), var(--brand-red));
  }
  .back__wordmark {
    position: absolute; left: 0; width: 100%; top: 226px;
    font-size: 50px; font-weight: 800; letter-spacing: 3px; color: var(--paper-text);
  }
  .tagline {
    position: absolute; left: 0; width: 100%; top: 306px;
    font-size: 15px; font-weight: 400; line-height: 21px;
  }
</style>
</head>
<body>
  <section class="card card--front">
    <div class="front__item name-first">FIRSTNAME</div>
    <div class="front__item name-last">LASTNAME</div>
    <div class="front__item job-title">DIRECTOR</div>
    <div class="divider divider--top"></div>

    <svg class="contact-icon contact-icon--phone" viewBox="0 0 18 18" aria-hidden="true">
      <circle cx="9" cy="9" r="9" fill="var(--brand-red)"/>
      <path d="M6.2 4.6l1.4 1.9-.9 1.1c.6 1.3 1.5 2.2 2.8 2.8l1.1-.9 1.9 1.4-.8 1.6c-3.6-.3-6.3-3-6.6-6.6z" fill="#fff"/>
    </svg>
    <div class="front__item contact-text contact-text--phone">123 456 7890</div>

    <svg class="contact-icon contact-icon--mail" viewBox="0 0 18 18" aria-hidden="true">
      <circle cx="9" cy="9" r="9" fill="var(--brand-red)"/>
      <rect x="4.5" y="6" width="9" height="6.2" fill="none" stroke="#fff" stroke-width="1.1"/>
      <path d="M4.5 6l4.5 3.4L13.5 6" fill="none" stroke="#fff" stroke-width="1.1"/>
    </svg>
    <div class="front__item contact-text contact-text--mail">EMAIL@DOMAINNAME.COM</div>

    <svg class="contact-icon contact-icon--web" viewBox="0 0 18 18" aria-hidden="true">
      <circle cx="9" cy="9" r="9" fill="var(--brand-red)"/>
      <g fill="none" stroke="#fff" stroke-width="0.9">
        <circle cx="9" cy="9" r="4.8"/>
        <ellipse cx="9" cy="9" rx="2" ry="4.8"/>
        <path d="M4.2 9h9.6M5 6.6h8M5 11.4h8"/>
      </g>
    </svg>
    <div class="front__item contact-text contact-text--web">WWW.DULVAN.COM</div>

    <div class="divider divider--bottom"></div>
    <div class="front__item wordmark">DULVAN</div>
  </section>

  <section class="card card--back">
    <div class="ring-art" role="img" aria-label="Line drawing of tree growth rings in the corner"></div>
    <div class="back__wordmark">DULVAN</div>
    <div class="tagline">fire equipment and parts<br>tree clearing</div>
    <div class="flame-art" role="img" aria-label="Outline drawing of flames along the bottom edge"></div>
  </section>
</body>
</html>
```